stationary for a modern hotel
Venmiro Hotels
Project: stationary for a modern hotel
stationary for a modern hotel - Hospitality Industry
Creative Brief
Use same font as used in my logo
anything that can go very well with my logo
Simple
Tundeyemi Okafordike
G.M
Venmiro Hotels Plot 318,Adebanjo-Ekwueme Way,Garki District Abuja Nigeria
tunde@venmirohotels.com
www.venmirohotels.com

```html
<!DOCTYPE html>
<html lang="en">
<head>
<meta charset="utf-8">
<title>Venmiro Hotels – Business Card</title>
<link href="https://fonts.googleapis.com/css2?family=Didact+Gothic&display=swap" rel="stylesheet">
<style>
  :root {
    --bg: #ece8e2;
    --tan: #b0895c;
    --tan-dark: #8f6a40;
    --paper: #ffffff;
    --ink: #6b6b6b;
    --rule: #c9c9c9;
  }
  * { margin: 0; padding: 0; box-sizing: border-box; }
  html, body {
    width: 1200px; height: 914px; overflow: hidden;
    background: var(--bg);
    font-family: "Didact Gothic", "Century Gothic", sans-serif;
  }
  .business-card {
    position: absolute; left: 100px; top: 162px;
    width: 1000px; height: 590px;
    background: var(--tan);
    padding: 26px;
    box-shadow: 0 6px 18px rgba(0,0,0,0.12);
  }
  .card-face {
    position: relative; width: 100%; height: 100%;
    background: var(--paper);
  }
  .brand {
    position: absolute; top: 118px; left: 0; right: 0;
    display: flex; justify-content: center; align-items: center; gap: 18px;
  }
  .brand-dot {
    width: 16px; height: 16px; border-radius: 50%; background: var(--tan);
  }
  .brand-name {
    font-size: 52px; letter-spacing: 3px; color: var(--tan);
    text-transform: uppercase;
  }
  .details {
    position: absolute; top: 300px; left: 0; right: 0;
    display: flex; justify-content: center;
  }
  .person {
    width: 420px; text-align: right; padding-right: 28px;
    color: var(--ink);
  }
  .person-name { font-size: 22px; color: var(--tan); }
  .person-title { font-size: 15px; margin-top: 6px; }
  .address { font-size: 15px; line-height: 1.55; margin-top: 26px; }
  .divider {
    width: 1px; background: var(--rule); height: 170px; margin-top: 40px;
  }
  .contacts {
    width: 420px; padding-left: 28px; list-style: none;
    padding-top: 40px; color: var(--ink); font-size: 15px;
  }
  .contacts li {
    display: flex; align-items: center; gap: 12px; height: 32px;
  }
  .contact-icon { width: 18px; height: 18px; flex: none; }
</style>
</head>
<body>
  <div class="business-card">
    <div class="card-face">
      <div class="brand">
        <span class="brand-dot"></span>
        <span class="brand-name">Venmiro Hotels</span>
      </div>

      <div class="details">
        <div class="person">
          <div class="person-name">Tundeyemi Okafordike</div>
          <div class="person-title">G.M</div>
          <div class="address">
            Venmiro Hotels<br>
            Plot 318,Adebanjo-Ekwueme Way,<br>
            Garki District Abuja Nigeria
          </div>
        </div>

        <div class="divider"></div>

        <ul class="contacts">
          <li>
            <svg class="contact-icon" viewBox="0 0 18 18" aria-hidden="true">
              <circle cx="9" cy="9" r="9" fill="var(--tan)"/>
              <path d="M6 4.5h2l.8 2.2-1.2.9a6 6 0 0 0 2.8 2.8l.9-1.2 2.2.8v2c0 .6-.5 1-1 1A8 8 0 0 1 5 5.5c0-.5.4-1 1-1z" fill="#fff"/>
            </svg>
            +2348031574462
          </li>
          <li>
            <svg class="contact-icon" viewBox="0 0 18 18" aria-hidden="true">
              <circle cx="9" cy="9" r="9" fill="var(--tan)"/>
              <path d="M6 4.5h2l.8 2.2-1.2.9a6 6 0 0 0 2.8 2.8l.9-1.2 2.2.8v2c0 .6-.5 1-1 1A8 8 0 0 1 5 5.5c0-.5.4-1 1-1z" fill="#fff"/>
            </svg>
            +2348094826153
          </li>
          <li>
            <svg class="contact-icon" viewBox="0 0 18 18" aria-hidden="true">
              <circle cx="9" cy="9" r="9" fill="var(--tan)"/>
              <rect x="4.5" y="6" width="9" height="6.5" fill="#fff"/>
              <path d="M4.5 6l4.5 3.6L13.5 6" fill="none" stroke="var(--tan)" stroke-width="1"/>
            </svg>
            tunde@venmirohotels.com
          </li>
          <li>
            <svg class="contact-icon" viewBox="0 0 18 18" aria-hidden="true">
              <circle cx="9" cy="9" r="9" fill="var(--tan)"/>
              <circle cx="9" cy="9" r="4.6" fill="none" stroke="#fff" stroke-width="1.1"/>
              <ellipse cx="9" cy="9" rx="2" ry="4.6" fill="none" stroke="#fff" stroke-width="1"/>
              <line x1="4.4" y1="9" x2="13.6" y2="9" stroke="#fff" stroke-width="1"/>
            </svg>
            www.venmirohotels.com
          </li>
        </ul>
      </div>
    </div>
  </div>
</body>
</html>
```